card design for engineering consultancy

engineering drafting and project management company the provides drafting services for.
Electrical, Hydraulic, Mechanical, and Civil services
The company is called K7R Services and logo is as attached
Information on card should be.
1. Logo
2.website : K7RServices.com
3. email : info@K7RServices.com
4. Phone: (+61) 400512738
5. Motto: Design - Document - Develop - Deliver

this card should be basically used for business identification only

Target Market(s)

electricians plumbers air conditioning installers and civil contractors

Industry/Entity Type

engineering, drafting, electrical, plumbing, airconditioning, civil

Contact Information for Business Card

1. Logo 2.website : K7RServices.com 3. email : info@K7RServices.com 4. Phone: (+61) 400512738 5. Motto: Design - Document - Develop - Deliver

Font styles to use
Serif

Requirements
Must have
• logo
Nice to have
• something inovative and different that makes it stand out from being just another business card

```html
<!DOCTYPE html>
<html lang="en">
<head>
<meta charset="utf-8">
<title>K7R Services – Business Card</title>
<link rel="stylesheet" href="https://fonts.googleapis.com/css2?family=Montserrat:wght@400;500;600;700&display=swap">
<style>
  :root {
    --backdrop: #2a2a2c;
    --card: #1d1d1f;
    --card-edge: #262628;
    --silver: #b9b9bb;
    --grey-mark: #8a8a8a;
    --white: #f1f1f1;
    --red: #d8262a;
    --muted: #e4e4e4;
  }
  * { margin: 0; padding: 0; box-sizing: border-box; }
  html, body {
    width: 1200px;
    height: 1095px;
    overflow: hidden;
    background: var(--backdrop);
    font-family: "Montserrat", sans-serif;
  }
  .canvas {
    position: relative;
    width: 1200px;
    height: 1095px;
  }
  .card {
    position: absolute;
    left: 220px;
    width: 760px;
    height: 434px;
    background: var(--card);
    border: 1px solid var(--card-edge);
    border-radius: 20px;
    box-shadow: 0 18px 40px rgba(0,0,0,.45);
    overflow: hidden;
  }
  .card--front { top: 82px; }
  .card--back { top: 580px; }

  /* Brand name lockup */
  .brand {
    display: flex;
    align-items: center;
    gap: 14px;
    font-weight: 600;
    letter-spacing: 0.14em;
    text-transform: uppercase;
  }
  .brand__square {
    background: var(--grey-mark);
    border-radius: 6px;
  }

  /* Front */
  .card--front .brand {
    position: absolute;
    left: 50%;
    top: 150px;
    transform: translateX(-50%);
    font-size: 44px;
    color: var(--silver);
    white-space: nowrap;
  }
  .card--front .brand__square { width: 48px; height: 48px; }
  .motto {
    position: absolute;
    left: 0;
    right: 0;
    bottom: 70px;
    text-align: center;
    font-weight: 700;
    font-size: 19px;
    letter-spacing: 0.04em;
    color: var(--white);
  }
  .motto__sep { color: var(--red); margin: 0 8px; font-weight: 500; }

  /* Back */
  .card--back .brand {
    position: absolute;
    right: 54px;
    top: 56px;
    font-size: 32px;
    color: var(--grey-mark);
  }
  .card--back .brand__square { width: 36px; height: 36px; background: var(--red); border-radius: 4px; }
  .rule {
    position: absolute;
    left: 230px;
    right: 54px;
    top: 150px;
    height: 1px;
    background: var(--red);
  }
  .person {
    position: absolute;
    left: 62px;
    top: 212px;
  }
  .person__name {
    font-size: 30px;
    font-weight: 500;
    letter-spacing: 0.04em;
    color: var(--red);
    text-transform: uppercase;
  }
  .person__role {
    font-size: 17px;
    font-weight: 500;
    color: var(--muted);
    margin-top: 4px;
  }
  .person__divider {
    width: 200px;
    height: 1px;
    background: var(--red);
    margin: 12px 0 10px;
  }
  .contacts { list-style: none; }
  .contacts li {
    display: flex;
    align-items: center;
    gap: 10px;
    font-size: 18px;
    font-weight: 500;
    color: var(--muted);
    letter-spacing: 0.02em;
    line-height: 1.6;
  }
  .contacts svg { width: 16px; height: 16px; fill: var(--red); flex: none; }
</style>
</head>
<body>
<main class="canvas">

  <section class="card card--front" aria-label="Card front">
    <div class="brand"><span class="brand__square"></span>K7R Services</div>
    <p class="motto">DESIGN<span class="motto__sep">|</span>DOCUMENT<span class="motto__sep">|</span>DEVELOP<span class="motto__sep">|</span>DELIVER</p>
  </section>

  <section class="card card--back" aria-label="Card back">
    <div class="brand"><span class="brand__square"></span>K7R Services</div>
    <div class="rule"></div>
    <div class="person">
      <h1 class="person__name">Mara Lindqvist</h1>
      <p class="person__role">Manager</p>
      <div class="person__divider"></div>
      <ul class="contacts">
        <li>
          <svg viewBox="0 0 24 24" aria-hidden="true"><path d="M6.6 10.8a15.1 15.1 0 0 0 6.6 6.6l2.2-2.2c.3-.3.7-.4 1-.2 1.1.4 2.3.6 3.6.6.6 0 1 .4 1 1V20c0 .6-.4 1-1 1C10.6 21 3 13.4 3 4c0-.6.4-1 1-1h3.5c.6 0 1 .4 1 1 0 1.3.2 2.5.6 3.6.1.3 0 .7-.2 1z"/></svg>
          (+61) 400512738
        </li>
        <li>
          <svg viewBox="0 0 24 24" aria-hidden="true"><path d="M2 5h20v14H2zm2 2v.5l8 5 8-5V7zm0 2.8V17h16V9.8l-8 5z"/></svg>
          info@K7RServices.com
        </li>
        <li>
          <svg viewBox="0 0 24 24" aria-hidden="true"><path d="M12 2a10 10 0 1 0 0 20 10 10 0 0 0 0-20zm6.9 6h-2.9a15.7 15.7 0 0 0-1.4-3.6A8 8 0 0 1 18.9 8zM12 4c.8 1.2 1.5 2.5 1.9 4h-3.8c.4-1.5 1.1-2.8 1.9-4zM4.3 14a8 8 0 0 1 0-4h3.4a16.5 16.5 0 0 0 0 4zm.8 2h2.9c.3 1.3.8 2.5 1.4 3.6A8 8 0 0 1 5.1 16zM8 8H5.1a8 8 0 0 1 4.3-3.6C8.8 5.5 8.3 6.7 8 8zm4 12c-.8-1.2-1.5-2.5-1.9-4h3.8c-.4 1.5-1.1 2.8-1.9 4zm2.3-6H9.7a14.7 14.7 0 0 1 0-4h4.6a14.7 14.7 0 0 1 0 4zm.3 5.6c.6-1.1 1.1-2.3 1.4-3.6h2.9a8 8 0 0 1-4.3 3.6zm1.7-5.6a16.5 16.5 0 0 0 0-4h3.4a8 8 0 0 1 0 4z"/></svg>
          K7RServices.com
        </li>
      </ul>
    </div>
  </section>

</main>
</body>
</html>
```